Speisekarten-Design für Café
Zielgruppe
Café mit Angebot von Frühstück und Torten/Kuchen (BIO!) und Verkauf von Dekoartikeln. Zielgruppe sind sowohl Familien, als auch ältere Personen, die sich zum Kaffeeklatsch treffen. Ebenso 'Freundinnen' und junge Mütter.
In den Räumlichkeiten war schon seit 24 Jahren ein Café, die Besitzerin ist aber verstorben
Aufgabenstellung
Karte in DIN A 5 Format, da die Tische nicht so groß sind. Die erste Seite soll die 'Geschichte' der Lokalität enthalten. Keine 'bunten' Bilder (Comics) von irgendwelchen Torten und/oder Frühstücken

```html
<!DOCTYPE html>
<html lang="de">
<head>
<meta charset="utf-8">
<title>Speisekarte – Haus Lindenhof</title>
<link rel="stylesheet" href="https://fonts.googleapis.com/css2?family=Great+Vibes&family=Merriweather:wght@300;400&display=swap">
<style>
  :root {
    --magenta: #a4307a;
    --magenta-soft: #b14f8c;
    --sand: #d9d4ce;
    --ink: #2b2522;
    --ring: #5a4a40;
    --fold: #b8b3ae;
    --paper: #ffffff;
  }
  * { margin: 0; padding: 0; box-sizing: border-box; }
  html, body { width: 1200px; height: 567px; overflow: hidden; background: var(--paper); }
  .menu-spread { position: relative; width: 1200px; height: 567px; background: var(--paper); font-family: "Merriweather", Georgia, serif; color: var(--ink); }
  .panel { position: absolute; top: 0; width: 400px; height: 567px; overflow: hidden; }
  .panel--cover { left: 0; }
  .panel--welcome { left: 400px; border-left: 1px solid var(--fold); }
  .panel--about { left: 800px; border-left: 1px solid var(--fold); }

  .footer-band { position: absolute; left: 0; right: 0; top: 451px; bottom: 0; background: var(--sand); }
  .footer-rule { position: absolute; left: 0; right: 0; top: 446px; height: 5px; background: var(--magenta); }

  .stripe-header { position: absolute; left: 0; top: 0; width: 400px; height: 149px; background: var(--magenta-soft); }
  .stripe-edge { position: absolute; left: 0; top: 149px; width: 400px; height: 5px; background: var(--sand); }

  .script { font-family: "Great Vibes", cursive; color: var(--magenta); font-weight: 400; }

  .cover-title { position: absolute; left: 0; width: 400px; top: 186px; text-align: center; font-size: 70px; line-height: 1; }
  .cover-subtitle { position: absolute; left: 0; width: 400px; top: 262px; text-align: center; font-size: 9.5px; font-weight: 300; color: #4a4440; }

  .seal { position: absolute; top: 362px; left: 148px; width: 104px; height: 104px; border-radius: 50%; background: var(--paper); border: 2px solid var(--ring); display: flex; align-items: center; justify-content: center; font-size: 9.5px; font-weight: 400; color: var(--ink); white-space: nowrap; }

  .welcome-title { position: absolute; left: 0; width: 400px; top: 122px; text-align: center; font-size: 38px; line-height: 42px; }
  .welcome-text { position: absolute; left: 0; width: 400px; top: 216px; text-align: center; font-size: 9.2px; line-height: 16.2px; font-weight: 400; }
  .opening-hours { position: absolute; left: 0; width: 400px; top: 484px; text-align: center; font-size: 9.2px; font-weight: 400; }
  .opening-hours sup { font-size: 5.5px; }
  .contact-lines { position: absolute; left: 173px; top: 518px; font-size: 7.6px; font-weight: 300; line-height: 11.5px; }
  .contact-lines li { list-style: none; display: flex; align-items: center; gap: 6px; }
  .contact-lines svg { width: 7px; height: 7px; }

  .about-title { position: absolute; left: 0; width: 400px; top: 118px; text-align: center; font-size: 42px; line-height: 1; }
  .about-text { position: absolute; left: 83px; width: 235px; top: 171px; font-size: 9.4px; line-height: 16.2px; font-weight: 300; text-align: justify; }

  .footer-brand { position: absolute; left: 36px; top: 504px; font-size: 8px; font-weight: 400; color: var(--ink); white-space: nowrap; }
  .address { position: absolute; left: 130px; top: 504px; font-size: 7.6px; line-height: 11.6px; font-weight: 300; font-style: normal; }
  .online { position: absolute; left: 243px; top: 504px; font-size: 7.6px; line-height: 11.6px; font-weight: 300; }
  .online li { list-style: none; display: flex; align-items: center; gap: 6px; }
  .online svg { width: 6px; height: 6px; }
</style>
</head>
<body>
<main class="menu-spread">

  <section class="panel panel--cover">
    <div class="stripe-header" role="img" aria-label="Vertikales Streifenmuster in Magenta und hellerem Pink"></div>
    <div class="stripe-edge"></div>
    <h1 class="cover-title script">Speisekarte</h1>
    <p class="cover-subtitle">Frühstück &amp; Getränke</p>
    <div class="footer-rule"></div>
    <div class="footer-band"></div>
    <div class="seal">Haus Lindenhof</div>
  </section>

  <section class="panel panel--welcome">
    <h2 class="welcome-title script">Genießen Sie<br>Ihre Zeit bei uns!</h2>
    <p class="welcome-text">Bitte sagen Sie uns,<br>wenn Sie etwas vermissen. Für Anregungen, durch die<br>wir Ihren Besuch in unserem Café noch genussvoller<br>machen können, sind wir dankbar.</p>
    <div class="footer-rule"></div>
    <div class="footer-band"></div>
    <div class="seal">Haus Lindenhof</div>
    <p class="opening-hours">Unsere Öffnungszeiten: täglich 8 bis 13 Uhr und 14<sup>30</sup> bis 18 Uhr</p>
    <ul class="contact-lines">
      <li><svg viewBox="0 0 10 10" aria-hidden="true"><circle cx="5" cy="5" r="5" fill="#2b2522"/><path d="M3.2 2.6c.4-.3.8-.2 1 .2l.4.8c.1.3 0 .5-.2.7l-.3.2c.3.7.8 1.2 1.5 1.5l.2-.3c.2-.2.4-.3.7-.2l.8.4c.4.2.5.6.2 1-.4.5-1 .7-1.6.4C4.4 6.8 3.2 5.6 2.7 4.1c-.2-.6 0-1.1.5-1.5z" fill="#fff"/></svg>0 12 34 . 567 89 00</li>
      <li><svg viewBox="0 0 10 10" aria-hidden="true"><circle cx="5" cy="5" r="4.2" fill="none" stroke="#2b2522" stroke-width="1.4"/><rect x="3" y="3.4" width="4" height="3.2" fill="#2b2522"/></svg>0 12 34 . 567 89 00</li>
    </ul>
  </section>

  <section class="panel panel--about">
    <h2 class="about-title script">Über uns</h2>
    <p class="about-text">Lorem ipsum dolor sit amet, consetetur sadipscing elitr, sed diam nonumy eirmod tempor invidunt ut labore et dolore magna aliquyam erat, sed diam volup­tua. At vero eos et accusam et justo duo dolores et ea rebum. Stet clita kasd gubergren, no sea takimata sanctus est Lorem ipsum dolor sit amet. Lorem ipsum dolor sit amet, consetetur sadipscing elitr, sed diam nonumy eirmod tempor invidunt ut labore et dolore magna aliquyam erat, sed diam voluptua. At vero eos et accusam et justo duo dolores et ea rebum. Stet clita kasd gubergren, no sea takimata sanctus est Lorem ipsum dolor sit amet.</p>
    <div class="footer-rule"></div>
    <div class="footer-band"></div>
    <p class="footer-brand">Haus Lindenhof</p>
    <address class="address">Birkenallee 7<br>31000 Wiesenfeld</address>
    <ul class="online">
      <li><svg viewBox="0 0 10 10" aria-hidden="true"><circle cx="5" cy="5" r="5" fill="#2b2522"/><circle cx="5" cy="5" r="2" fill="#d9d4ce"/></svg>haus-lindenhof.de</li>
      <li><svg viewBox="0 0 10 10" aria-hidden="true"><circle cx="5" cy="5" r="5" fill="#2b2522"/></svg>social.example/haus-lindenhof</li>
    </ul>
  </section>

</main>
</body>
</html>
```